Northwind Sums Tutor

Need a new design for northwindsumstutor.example as we are having a new backend developed. The design should be fun, and visually interesting for kids, yet sophisticated enough for parents, teachers and school districts.

Our main competitor is qvo.example and we like their concept. The colors should pop, and be exciting. The layout should be simple. Because we are having our website developed, we only will need the design and no functionality, a Photoshop or Fireworks file will work best.

We like the simplicity of our existing site, but it looks fairly unexciting. Here is a version our developers gave us. We do not like the design.

http://velonbrightworks.example/velonlayout/northwindsumstutor/layout/

The winning designer will most likely get more work from us as we make modifications.

Target Market(s)

Parents, Teachers, students

Industry/Entity Type

School

Requirements
Must have
• login at the top
social icons for recommend and like
Showcase area for features and testimonials

```html
<!DOCTYPE html>
<html lang="en">
<head>
<meta charset="utf-8">
<title>Northwind Sums Tutor</title>
<link rel="stylesheet" href="https://fonts.googleapis.com/css2?family=Arimo:wght@400;700&family=Open+Sans:wght@400;600&family=Tinos&display=swap">
<style>
:root{
  --green-dark:#003300;
  --green:#005a00;
  --footer:#002800;
  --orange:#ff7a00;
  --orange-line:#f6b300;
  --peach:#ffc08a;
  --grey-bar:#5a5a5a;
  --panel-border:#d6d6d6;
  --text:#000;
  --blue-title:#0a5a8c;
  --card-red:#f08a8a;
  --card-blue:#7fa3e6;
  --card-lilac:#d8a0c8;
}
*{box-sizing:border-box;margin:0;padding:0}
html,body{width:1008px;height:1200px;overflow:hidden;background:#fff}
body{font-family:Arimo,Arial,sans-serif;color:var(--text)}
.page{position:relative;width:994px;height:1183px;transform:scale(1.0141);transform-origin:0 0;background:#fff}
.abs{position:absolute}

/* header */
.brand{left:10px;top:24px}
.brand-name{font-family:Arimo,Arial,sans-serif;font-size:21px;color:#333;display:flex;align-items:center;gap:6px}
.brand-name i{display:inline-block;width:12px;height:12px;background:var(--orange)}
.brand-tag{font-family:"Open Sans",sans-serif;font-size:13px;font-weight:600;margin-top:8px;color:#222}
.brand-tag em{font-style:normal;color:var(--orange)}
.login{left:445px;top:0;width:390px;height:47px;background:var(--grey-bar);border-radius:0 0 6px 6px;padding:2px 6px;color:#fff;font-size:11px}
.login-row{display:flex;gap:6px;margin-top:4px}
.field{background:#fff;border:1px solid #999;height:19px;color:#000;font-size:11px;padding:2px 3px}
.btn-sign{background:#eee;border:1px solid #888;color:#000;font-size:11px;height:19px;padding:1px 10px;border-radius:2px}
.remember{left:838px;top:0;width:152px;height:47px;background:var(--grey-bar);border-radius:0 0 6px 6px;color:#fff;font-size:13px;padding:8px 6px}
.remember span{display:inline-block;width:11px;height:11px;background:#fff;margin-right:3px;vertical-align:-1px}
.remember u{display:block;margin-top:2px}
.nav{top:56px;height:34px;color:#fff;font-weight:700;font-size:13px;display:flex;align-items:center;justify-content:center;letter-spacing:.4px;background:var(--green)}
.nav.active{background:var(--green-dark)}
.divider{left:0;top:108px;width:994px;height:8px;background:linear-gradient(#e8e8e8,#f6f6f6)}

/* hero */
.support-icon{left:612px;top:122px;width:50px;height:50px;background:var(--orange);border-radius:10px}
.support{left:685px;top:120px;font-family:Tinos,serif;font-size:18px;line-height:28px}
.support b{font-weight:400}
.support .num{color:#999}
.hero{left:12px;top:140px;width:475px;height:297px;border:3px solid var(--panel-border);border-radius:10px;background:#fff;overflow:hidden}
.hero-art{position:absolute;left:2px;top:2px;width:465px;height:238px;background:linear-gradient(135deg,#fdfbe0,#e4f3c4 60%,#d8ecf7)}
.hero-title{position:absolute;left:14px;top:10px;font-family:"Open Sans",sans-serif;font-size:22px;color:var(--blue-title);font-weight:600}
.hero-sub{position:absolute;left:14px;top:38px;font-size:13px;font-weight:700;color:#2a8ad0}
.hero-foot{position:absolute;left:2px;top:242px;width:465px;height:48px;background:#eee;font-family:"Open Sans",sans-serif;font-size:23px;padding:8px 18px;color:#222}
.hero-foot em{font-style:normal;color:var(--orange)}
.intro{left:501px;top:197px;width:474px;height:238px;border:3px solid var(--panel-border);border-radius:10px;padding:7px 6px;font-size:13.4px;line-height:16.8px;color:#111}

/* features */
.features{left:12px;top:455px;width:964px;height:307px;border:3px solid var(--panel-border);border-radius:10px}
.section-title{height:24px;color:#fff;font-family:"Open Sans",sans-serif;font-weight:600;font-size:15px;padding:2px 8px;background:var(--green)}
.card{width:208px;height:116px;border:3px solid var(--card-red);background:#fff;box-shadow:0 3px 3px #bbb;padding:12px 12px;font-family:"Open Sans",sans-serif}
.card.blue{border-color:var(--card-blue)}
.card.lilac{border-color:var(--card-lilac)}
.card h3{font-weight:400;font-size:17px;color:#333}
.card p{font-size:10px;line-height:12.5px;width:118px;margin-top:6px;color:#222}
.card a{display:block;font-size:10px;font-weight:600;color:#1c4f8a;text-decoration:underline;margin-top:8px}
.card .kid{position:absolute;right:10px;top:14px;width:40px;height:78px;background:#f2d6c8;border-radius:18px 18px 6px 6px}

/* bottom */
.lower{left:12px;top:772px;width:966px;height:296px;background:#ececec;box-shadow:0 2px 6px #aaa;border:1px solid #ddd}
.lower-inner{left:25px;top:785px;width:938px;height:261px;background:#fff}
.col-text{font-size:10.5px;line-height:13px}
.vrule{top:835px;height:205px;border-left:1px dotted #444}
.testi{left:432px;width:264px;height:42px;background:var(--peach);font-size:10.5px;line-height:13px;padding:2px 4px 0 46px;position:absolute}
.testi .cal{position:absolute;left:3px;top:5px;width:38px;height:30px;background:#ddd;border-top:7px solid #c0282d}
.map{left:735px;top:918px;width:222px;height:108px;background:radial-gradient(ellipse at 50% 50%,#8cc34a,#a9d46e 60%,#fff 75%)}

/* footer */
.footer{left:0;top:1093px;width:994px;height:90px;background:var(--footer);color:#fff;font-size:13px}
.footer .links{position:absolute;left:37px;top:37px}
.footer .copy{position:absolute;left:417px;top:37px}
.follow{position:absolute;left:833px;top:26px;width:152px;height:40px;background:#eef3f6;color:#1d3a6e;font-weight:700;font-size:12px;padding:12px 6px;display:flex;align-items:center;gap:4px}
.follow i{display:inline-block;width:30px;height:30px;border-radius:5px;margin-top:-10px}
</style>
</head>
<body>
<div class="page">
  <header>
    <div class="abs brand">
      <div class="brand-name"><i></i>northwindsumstutor.example</div>
      <div class="brand-tag">It makes <em>Learning</em> Fun!</div>
    </div>
    <form class="abs login">
      <div>Sign in with our account:</div>
      <div class="login-row">
        <div class="field" style="width:154px">Username/Email</div>
        <div class="field" style="width:154px">••••••••</div>
        <div class="btn-sign">Sign In</div>
      </div>
    </form>
    <div class="abs remember"><span></span>Remember me<u>Create an account</u></div>
    <nav>
      <div class="abs nav active" style="left:657px;width:99px">HOME</div>
      <div class="abs nav" style="left:764px;width:98px">ABOUT US</div>
      <div class="abs nav" style="left:872px;width:99px">CONTACT US</div>
    </nav>
    <div class="abs divider"></div>
  </header>

  <svg class="abs" style="left:0;top:118px" width="994" height="72" viewBox="0 0 994 72">
    <polyline points="0,7 473,7 565,68 994,68" fill="none" stroke="var(--orange-line)" stroke-width="3"/>
  </svg>
  <div class="abs support-icon" role="img" aria-label="Support headset icon"></div>
  <div class="abs support"><b>SUPPORT:</b> <span class="num">(xxx) xxx-xxx</span><br><b>EMAIL:</b> xxxx@mailbox.example</div>

  <section class="abs hero">
    <div class="hero-art" role="img" aria-label="Illustration of two children among colourful numbers and math shapes"></div>
    <div class="hero-title">Math for the left and right brain</div>
    <div class="hero-sub">Comprehensive, dynamic content &gt;&gt;</div>
    <div class="hero-foot"><em>Education</em> is the <em>BEST</em> inverstment</div>
  </section>
  <p class="abs intro">Lorem Ipsum is simply dummy text of the printing and typesetting industry. Lorem Ipsum has been the industry's standard dummy text ever since the 1500s, when an unknown printer took a galley of type and scrambled it to make a type specimen book. It has survived not only five centuries, but also the leap into electronic typesetting, remaining essentially unchanged. Lorem Ipsum is simply dummy text of the printing and typesetting industry. Lorem Ipsum has been the industry's standard dummy text ever since the 1500s, when an unknown printer took a galley of type and scrambled it to make a type specimen book. It has survived not only five centuries, but also the leap into electronic typesetting, remaining essentially unchanged. Lorem Ipsum has been the industry's standard dummy text ever since the 1500s, when an unknown printer took a galley of type and scrambled it to make a type specimen book. It has survived not only five centuries.</p>

  <section class="abs features"></section>
  <div class="abs section-title" style="left:28px;top:461px;width:255px;padding-left:48px">Features</div>
  <svg class="abs" style="left:31px;top:463px" width="32" height="20"><ellipse cx="14" cy="12" rx="13" ry="7" fill="#cfe6f2"/><line x1="14" y1="12" x2="28" y2="2" stroke="var(--orange)" stroke-width="3"/></svg>

  <div class="abs card" style="left:28px;top:498px"><h3>Pre-K</h3><p>Counting dots, comparing groups, long and short, and more.</p><a>See all 41 skills &gt;&gt;</a><div class="kid" role="img" aria-label="Drawn girl in red dress"></div></div>
  <div class="abs card blue" style="left:267px;top:498px"><h3>Kindergarten</h3><p>Patterns, identifying shapes, skip-counting, and more.</p><a>See all 104 skills &gt;&gt;</a><div class="kid" role="img" aria-label="Drawn boy in blue shirt"></div></div>
  <div class="abs card lilac" style="left:506px;top:498px"><h3>First grade</h3><p>Bar graphs, addition word problems, counting coins, and more.</p><a>See all 151 skills &gt;&gt;</a><div class="kid" role="img" aria-label="Drawn girl in pink dress"></div></div>
  <div class="abs card" style="left:746px;top:498px"><h3>Pre-K</h3><p>Counting dots, comparing groups, long and short, and more.</p><a>See all 41 skills &gt;&gt;</a><div class="kid" role="img" aria-label="Drawn girl in red dress"></div></div>
  <div class="abs card" style="left:28px;top:633px"><h3>Pre-K</h3><p>Counting dots, comparing groups, long and short, and more.</p><a>See all 41 skills &gt;&gt;</a><div class="kid" role="img" aria-label="Drawn girl in red dress"></div></div>
  <div class="abs card blue" style="left:267px;top:633px"><h3>Kindergarten</h3><p>Patterns, identifying shapes, skip-counting, and more.</p><a>See all 104 skills &gt;&gt;</a><div class="kid" role="img" aria-label="Drawn boy in blue shirt"></div></div>
  <div class="abs card lilac" style="left:506px;top:633px"><h3>First grade</h3><p>Bar graphs, addition word problems, counting coins, and more.</p><a>See all 151 skills &gt;&gt;</a><div class="kid" role="img" aria-label="Drawn girl in pink dress"></div></div>
  <div class="abs card" style="left:746px;top:633px"><h3>Pre-K</h3><p>Counting dots, comparing groups, long and short, and more.</p><a>See all 41 skills &gt;&gt;</a><div class="kid" role="img" aria-label="Drawn girl in red dress"></div></div>

  <div class="abs lower"></div>
  <div class="abs lower-inner"></div>

  <svg class="abs" style="left:54px;top:798px" width="34" height="24"><polygon points="17,2 33,9 17,16 1,9" fill="#111"/><rect x="9" y="12" width="16" height="8" fill="#111"/></svg>
  <div class="abs section-title" style="left:88px;top:797px;width:286px">Welcome to our website</div>
  <p class="abs col-text" style="left:54px;top:827px;width:320px">Lorem Ipsum is simply dummy text of the printing and typesetting industry. Lorem Ipsum has been the industry's standard dummy text ever since the 1500s, when an unknown printer took a galley of type and scrambled it to make a type specimen book. It has survived not only five centuries, but also the leap into electronic typesetting, remaining essentially unchanged.  Lorem Ipsum is simply dummy text of the printing and typesetting industry. Lorem Ipsum has been the industry's standard dummy text ever since the 1500s, when an unknown printer took a galley of type and scrambled it to make a type specimen book. It has survived not only five centuries, but also the leap into electronic typesetting, remaining essentially unchanged.  Lorem Ipsum has been the industry's standard dummy text ever since the 1500s, when an unknown printer took a galley of type and scrambled it to make a type specimen book. It has survived not only five centuries, but also the leap into electronic typesetting.</p>
  <div class="abs vrule" style="left:410px"></div>

  <svg class="abs" style="left:433px;top:798px" width="30" height="24"><rect x="1" y="3" width="26" height="18" rx="2" fill="#888"/><rect x="4" y="7" width="20" height="11" fill="#ddd"/></svg>
  <div class="abs section-title" style="left:463px;top:797px;width:233px;background:var(--orange)">Testimonials</div>
  <div class="testi" style="top:832px"><span class="cal"></span>It is a long established fact that a reader will be distracted by the readable content of a page when looking at its layout.</div>
  <div class="testi" style="top:884px"><span class="cal"></span>It is a long established fact that a reader will be distracted by the readable content of a page when looking at its layout.</div>
  <div class="testi" style="top:936px"><span class="cal"></span>It is a long established fact that a reader will be distracted by the readable content of a page when looking at its layout.</div>
  <div class="testi" style="top:988px"><span class="cal"></span>It is a long established fact that a reader will be distracted by the readable content of a page when looking at its layout.</div>
  <div class="abs vrule" style="left:716px"></div>

  <svg class="abs" style="left:735px;top:795px" width="24" height="26"><circle cx="12" cy="10" r="9" fill="#999"/><circle cx="12" cy="10" r="4" fill="#333"/><rect x="5" y="20" width="14" height="4" fill="#999"/></svg>
  <div class="abs section-title" style="left:759px;top:797px;width:193px">Around the world</div>
  <p class="abs col-text" style="left:735px;top:833px;width:225px">Lorem Ipsum is simply dummy text of the printing and typesetting industry. Lorem Ipsum has been the industry's standard dummy text ever since the 1500s, when an unknown printer took a galley of type and scrambled it to make a type specimen book.</p>
  <div class="abs map" role="img" aria-label="World map in green tones"></div>

  <footer class="abs footer">
    <div class="links">Home | About Us | Contact Us</div>
    <div class="copy">copyright@2012 northwindsumstutor.example</div>
    <div class="follow">Follow Us on: <i style="background:#3b5b9a"></i><i style="background:#4fb0e0"></i></div>
  </footer>
</div>
</body>
</html>
```